Business Card Design for Varnok Facility Services

We are looking for a Business Card Design for the Company "Varnok Facility Services."
Front side:
- Company Logo (small)
- Company Name, address, pohone, website and personal data.
- white background, for text e.g. company colors (blue or green like in the logo)
Please use following data:
Company data:
Varnok Facility Services Tulbrecht
Kirchmattweg 12
6331 Cham
www.varnok-fs.ch
Person data:
Ruben Tulbrecht
Geschäftsführer
+41 76 519 84 60
info@varnok-fs.ch
Back side:
could be colored in blue or green
please use a big logo sing and some smaller icons to say what is all beeing offered in facility services, like cleaning, maintenance cleaning
industrial cleaning, caretaking, gardening, disposal. There is no need for everyone of the icons if there are similar or an icon is standing for more of them.
Cleaning Service
colors to use:
blue: HEX 246BB0
green: HEX 52B33E

```html
<!DOCTYPE html>
<html lang="de">
<head>
<meta charset="utf-8">
<title>Varnok Facility Services – Business Card</title>
<link rel="stylesheet" href="https://fonts.googleapis.com/css2?family=Lato:wght@400;700&family=Montserrat:wght@700&display=swap">
<style>
  :root {
    --brand-blue: #246bb0;
    --brand-blue-card: #2a74b8;
    --brand-green: #52b33e;
    --ink-grey: #666a6e;
    --paper: #ffffff;
    --stage: #e9ecef;
  }
  * { box-sizing: border-box; margin: 0; padding: 0; }
  html, body { width: 1200px; height: 1000px; overflow: hidden; }
  body {
    background: var(--stage);
    font-family: "Lato", Arial, sans-serif;
    position: relative;
  }
  .card {
    position: absolute;
    left: 220px;
    width: 760px;
    height: 434px;
    border-radius: 22px;
    overflow: hidden;
    box-shadow: 0 6px 18px rgba(0,0,0,0.15);
  }

  /* Back side */
  .card-back { top: 40px; background: var(--brand-blue-card); }
  .back-brand {
    position: absolute; top: 92px; left: 0; right: 0;
    display: flex; align-items: center; justify-content: center; gap: 22px;
  }
  .brand-dot {
    width: 70px; height: 70px; border-radius: 50%;
    background: var(--brand-green);
  }
  .back-brand .brand-name {
    color: var(--paper); font-size: 58px; font-weight: 700; letter-spacing: 4px; line-height: 1;
  }
  .back-brand .brand-tag {
    color: var(--brand-green); font-size: 22px; font-weight: 700; letter-spacing: 6px;
    text-transform: uppercase; margin-top: 6px;
  }
  .services {
    position: absolute; left: 44px; right: 44px; top: 270px;
    display: flex; justify-content: space-between; list-style: none;
  }
  .service { display: flex; flex-direction: column; align-items: center; gap: 12px; }
  .service-badge {
    width: 58px; height: 58px; border-radius: 50%;
    background: radial-gradient(circle at 40% 35%, #6cc957, var(--brand-green));
  }
  .service-label { color: var(--paper); font-size: 17px; white-space: nowrap; }

  /* Front side */
  .card-front { top: 526px; background: var(--paper); }
  .front-band { position: absolute; inset: 0; }
  .company {
    position: absolute; left: 46px; top: 40px; font-size: 30px; line-height: 1.15;
  }
  .company .company-lead { color: var(--brand-green); display: block; }
  .company .company-rest { color: var(--ink-grey); display: block; }
  .address {
    position: absolute; left: 46px; top: 128px; color: var(--ink-grey); font-size: 17px; line-height: 1.3;
  }
  .front-brand {
    position: absolute; right: 44px; top: 130px; text-align: right;
  }
  .front-brand .brand-name {
    color: var(--brand-blue); font-size: 44px; font-weight: 700; letter-spacing: 3px; line-height: 1;
  }
  .front-brand .brand-tag {
    color: var(--brand-green); font-size: 16px; font-weight: 700; letter-spacing: 5px;
    text-transform: uppercase; margin-top: 4px;
  }
  .front-mark {
    position: absolute; right: 60px; top: 260px;
    width: 130px; height: 130px; border-radius: 50%;
    background: var(--paper);
  }
  .person { position: absolute; left: 46px; top: 240px; color: var(--paper); }
  .person-name {
    font-family: "Montserrat", Arial, sans-serif; font-size: 22px; font-weight: 700;
    letter-spacing: 1px; text-transform: uppercase;
  }
  .person-role { font-size: 18px; margin-top: 2px; }
  .contact { list-style: none; margin-top: 16px; font-size: 19px; line-height: 1.55; }
  .contact li { display: flex; align-items: center; gap: 12px; }
  .contact svg { width: 16px; height: 16px; fill: var(--paper); flex: none; }
</style>
</head>
<body>

<section class="card card-back" aria-label="Card back">
  <div class="back-brand">
    <span class="brand-dot"></span>
    <div>
      <div class="brand-name">Varnok</div>
      <div class="brand-tag">Facility Services</div>
    </div>
  </div>
  <ul class="services">
    <li class="service"><span class="service-badge" role="img" aria-label="Icon: people doing maintenance cleaning"></span><span class="service-label">Maintenance cleaning</span></li>
    <li class="service"><span class="service-badge" role="img" aria-label="Icon: worker with cleaning machine"></span><span class="service-label">Industrial cleaning</span></li>
    <li class="service"><span class="service-badge" role="img" aria-label="Icon: hand holding a heart"></span><span class="service-label">Caretaking</span></li>
    <li class="service"><span class="service-badge" role="img" aria-label="Icon: gardener with plants"></span><span class="service-label">Gardening</span></li>
    <li class="service"><span class="service-badge" role="img" aria-label="Icon: person with waste bin"></span><span class="service-label">Disposal</span></li>
  </ul>
</section>

<section class="card card-front" aria-label="Card front">
  <svg class="front-band" viewBox="0 0 760 434" preserveAspectRatio="none" aria-hidden="true">
    <path d="M0 210 L760 300 L760 434 L0 434 Z" fill="var(--brand-blue-card)"/>
  </svg>

  <p class="company">
    <span class="company-lead">Varnok Facility</span>
    <span class="company-rest">Services Tulbrecht</span>
  </p>
  <p class="address">Kirchmattweg 12<br>6331 Cham</p>

  <div class="front-brand">
    <div class="brand-name">Varnok</div>
    <div class="brand-tag">Facility Services</div>
  </div>
  <span class="front-mark" aria-hidden="true"></span>

  <div class="person">
    <div class="person-name">Ruben Tulbrecht</div>
    <div class="person-role">Geschäftsführer</div>
    <ul class="contact">
      <li><svg viewBox="0 0 16 16"><path d="M3.5 1l2.5 3-1.5 1.8c.9 2 2.7 3.8 4.7 4.7L11 9l3 2.5-1.3 2.5C7 14 2 9 2 3.3z"/></svg>+41 76 519 84 60</li>
      <li><svg viewBox="0 0 16 16"><path d="M1 3h14v10H1zM2.5 4.5v.4L8 9l5.5-4.1v-.4zM2.5 6.7v4.8h11V6.7L8 10.8z" fill-rule="evenodd"/></svg>info@varnok-fs.ch</li>
      <li><svg viewBox="0 0 16 16"><circle cx="8" cy="8" r="7"/></svg>www.varnok-fs.ch</li>
    </ul>
  </div>
</section>

</body>
</html>
```